Stickers signage for the outside of a 24 foot box truck.

This truck is for an oil field service truck, I have included a picture of the truck and the logo. The service is steam, heating and pressure washing for the oil field. Because of the large area to use for branding and advertising, I would like to have large decals placed on the truck, but not a full wrap due to the cost and the style is not what we are looking for.

I would like a series of large decals with log, phone number, email and some of the words mentioned, steam, heating, pressure washing place on. I would like some creativity in using the logo and graphics that compliment the logo. We are looking for edgy, and simplistic at the same time. Many truck wraps have so many things going on, the brand is lost. I have posted as well as example of a brand well recognized in the industry. Though I am not personally a fan of the truck design, it is well recognized instantly, and repeatable on each truck.

Given the name of the company Falcon Ridge, this gives the designer some leeway in using that in the design.

Sides, front, and back all available for signage.

Please only submit one design, unless the designs are completely different. I am looking for unique designs from different designers, and on one task done here, there were numerous similar designs submitted. Thank you for your submissions, all your hard work is appreciated.

There is a company called Teal Oilfield Services, they have a brand, recognizable and memorable. Very well designed. Also the task is now guaranteed.

0192cc
000000
ffffff

```html
<!DOCTYPE html>
<html lang="en">
<head>
<meta charset="utf-8">
<title>Falcon Ridge Oilfield Services Limited – Truck Decals</title>
<link rel="stylesheet" href="https://fonts.googleapis.com/css2?family=Orbitron:wght@500;700&display=swap">
<style>
  :root {
    --brand-blue: #0192cc;
    --panel-black: #1e1b1c;
    --white: #ffffff;
    --page: #ffffff;
  }
  html, body {
    margin: 0;
    padding: 0;
    overflow: hidden;
    background: var(--page);
  }
  .canvas {
    position: relative;
    width: 1200px;
    height: 826px;
    background: var(--page);
    overflow: hidden;
    font-family: "Orbitron", sans-serif;
  }
  .decal {
    position: absolute;
    left: 57px;
    width: 1086px;
    background: var(--panel-black);
  }
  .decal--brand   { top: 33px;  height: 199px; }
  .decal--washing { top: 240px; height: 181px; }
  .decal--heating { top: 432px; height: 181px; }
  .decal--steam   { top: 624px; height: 186px; }

  .brand-mark {
    position: absolute;
    left: 55px;
    top: 12px;
    width: 185px;
    height: 172px;
    background: var(--white);
  }
  .brand-name {
    position: absolute;
    left: 265px;
    top: 42px;
    margin: 0;
    font-size: 74px;
    font-weight: 700;
    line-height: 1;
    color: var(--white);
    letter-spacing: 2px;
    white-space: nowrap;
  }
  .brand-tagline {
    position: absolute;
    left: 267px;
    top: 136px;
    margin: 0;
    font-size: 25px;
    font-weight: 500;
    line-height: 1;
    color: var(--brand-blue);
    letter-spacing: 13px;
    white-space: nowrap;
  }

  .service-icon {
    position: absolute;
    left: 58px;
    top: 12px;
    width: 183px;
    height: 158px;
    background: linear-gradient(to bottom, var(--white) 0%, var(--white) 45%, var(--brand-blue) 60%, var(--brand-blue) 100%);
  }
  .decal--steam .service-icon { height: 162px; }

  .service-title {
    position: absolute;
    left: 270px;
    top: 52px;
    margin: 0;
    font-size: 50px;
    font-weight: 500;
    line-height: 1;
    color: var(--white);
    letter-spacing: 1px;
    white-space: nowrap;
  }
  .service-subtitle {
    position: absolute;
    left: 270px;
    top: 113px;
    margin: 0;
    font-size: 27px;
    font-weight: 500;
    line-height: 1;
    color: var(--brand-blue);
    letter-spacing: 1px;
    white-space: nowrap;
  }
  .decal--steam .service-title { top: 56px; }
  .decal--steam .service-subtitle { top: 117px; }
</style>
</head>
<body>
  <main class="canvas">
    <section class="decal decal--brand">
      <div class="brand-mark" aria-hidden="true"></div>
      <h1 class="brand-name">FALCON RIDGE</h1>
      <p class="brand-tagline">OILFIELD SERVICES LIMITED</p>
    </section>

    <section class="decal decal--washing">
      <div class="service-icon" role="img" aria-label="Pressure washer nozzle spraying, white over blue water"></div>
      <h2 class="service-title">PRESSURE WASHING</h2>
      <p class="service-subtitle">DEEP PRESSURE WASH</p>
    </section>

    <section class="decal decal--heating">
      <div class="service-icon" role="img" aria-label="Flames rising from blue water"></div>
      <h2 class="service-title">HEATING</h2>
      <p class="service-subtitle">HEAT CLEAN</p>
    </section>

    <section class="decal decal--steam">
      <div class="service-icon" role="img" aria-label="Cloud of steam rising from blue water"></div>
      <h2 class="service-title">STEAM</h2>
      <p class="service-subtitle">LIFT THE DIRT</p>
    </section>
  </main>
</body>
</html>
```